TLR Property - Business Cards

Looking for a business card & general letterhead, signage etc design for our new logo.

Colours:
000a20
0056a2
00b5ef
0088ce
68cef2

Fonts:
Poppins
Karla

Please keep look and feel of new brand - example in the zip package I sent.

```html
<!DOCTYPE html>
<html lang="en">
<head>
<meta charset="utf-8">
<title>TLR Property – Business Cards</title>
<link href="https://fonts.googleapis.com/css2?family=Karla:wght@400;500&family=Poppins:wght@500;600;700&display=swap" rel="stylesheet">
<style>
  :root {
    --navy: #000a20;
    --brand-blue: #0056a2;
    --mid-blue: #0088ce;
    --band-blue: #2089cf;
    --sky: #00b5ef;
    --light-sky: #68cef2;
    --paper: #ffffff;
    --ink: #4a4f57;
    --stage: #e9ebee;
  }
  * { margin: 0; padding: 0; box-sizing: border-box; }
  html, body { width: 1200px; height: 1129px; overflow: hidden; }
  body {
    background: var(--stage);
    position: relative;
    font-family: "Karla", sans-serif;
  }
  .card {
    position: absolute;
    left: 180px;
    width: 840px;
    height: 480px;
    overflow: hidden;
    box-shadow: 0 10px 30px rgba(0, 10, 32, 0.18);
  }
  .card-back { top: 60px; }
  .card-front { top: 590px; background: var(--paper); }

  .back-pattern {
    position: absolute;
    inset: 0;
    background: linear-gradient(135deg, #3a9fd8 0%, var(--mid-blue) 30%, var(--brand-blue) 75%, #0a4a98 100%);
  }

  .front-shape { position: absolute; inset: 0; }

  .wordmark {
    position: absolute;
    left: 96px;
    top: 92px;
    font-family: "Poppins", sans-serif;
    font-weight: 600;
    font-size: 46px;
    color: var(--brand-blue);
    display: flex;
    align-items: center;
    gap: 16px;
  }
  .wordmark-dot {
    width: 26px;
    height: 26px;
    border-radius: 50%;
    background: var(--light-sky);
  }

  .person {
    position: absolute;
    right: 150px;
    top: 196px;
    text-align: right;
  }
  .person-name {
    font-family: "Poppins", sans-serif;
    font-weight: 700;
    font-size: 27px;
    letter-spacing: 0.5px;
    color: var(--brand-blue);
    line-height: 1.1;
  }
  .person-role {
    font-family: "Karla", sans-serif;
    font-size: 22px;
    color: var(--light-sky);
    line-height: 1.2;
  }

  .contact {
    position: absolute;
    left: 96px;
    bottom: 58px;
    color: var(--ink);
    font-size: 19px;
    line-height: 1.3;
  }
  .contact-address { margin-bottom: 10px; }
  .contact-list { list-style: none; }
  .contact-list li { display: flex; align-items: center; gap: 10px; }
  .contact-icon { width: 18px; height: 18px; flex: none; }
</style>
</head>
<body>

  <section class="card card-back">
    <div class="back-pattern" role="img" aria-label="Repeating brand symbol pattern in blue tones with one white symbol highlighted"></div>
  </section>

  <section class="card card-front">
    <svg class="front-shape" viewBox="0 0 840 480" preserveAspectRatio="none" aria-hidden="true">
      <rect width="840" height="480" fill="var(--band-blue)"/>
      <path d="M0,0 L560,0 C760,60 800,300 770,480 L0,480 Z" fill="var(--paper)"/>
      <path d="M712,140 C790,250 808,380 792,480 L738,480 C764,380 758,260 712,140 Z" fill="var(--light-sky)"/>
    </svg>

    <div class="wordmark">
      <span class="wordmark-dot"></span>
      <span>TLR Property</span>
    </div>

    <div class="person">
      <p class="person-name">DORIAN VELLASO</p>
      <p class="person-role">Managing Director</p>
    </div>

    <div class="contact">
      <p class="contact-address">718 W Harlow St<br>Lindenvale, CA 90412</p>
      <ul class="contact-list">
        <li>
          <svg class="contact-icon" viewBox="0 0 24 24" aria-hidden="true"><path fill="var(--brand-blue)" d="M6.6 10.8a15.1 15.1 0 0 0 6.6 6.6l2.2-2.2a1 1 0 0 1 1-.25 11.4 11.4 0 0 0 3.6.57 1 1 0 0 1 1 1V20a1 1 0 0 1-1 1A17 17 0 0 1 3 4a1 1 0 0 1 1-1h3.5a1 1 0 0 1 1 1c0 1.25.2 2.45.57 3.6a1 1 0 0 1-.25 1z"/></svg>
          <span>(555) 210-4417</span>
        </li>
        <li>
          <svg class="contact-icon" viewBox="0 0 24 24" aria-hidden="true"><rect x="2" y="5" width="20" height="14" rx="2" fill="var(--brand-blue)"/><path d="M3 6l9 7 9-7" fill="none" stroke="#fff" stroke-width="1.6"/></svg>
          <span>info@tlrproperty.com</span>
        </li>
        <li>
          <svg class="contact-icon" viewBox="0 0 24 24" aria-hidden="true"><circle cx="12" cy="12" r="10" fill="var(--brand-blue)"/><path d="M2 12h20M12 2c3 3 3 17 0 20M12 2c-3 3-3 17 0 20" fill="none" stroke="#fff" stroke-width="1.3"/></svg>
          <span>www.tlrproperty.com</span>
        </li>
      </ul>
    </div>
  </section>

</body>
</html>
```